www.brightlingua.net -- International Language school needs a Wordpress Design

NOTE: This is for a complete WordPress website with coding (Design/develop)

We are a small, private English language school in business for 15 years. Our students come from around the world to study English at our centre in Toronto, Canada. Most of our students are in their 20's and come to study English with us for periods of 1-6 months before returning home to complete their post-secondary education or pursue their careers.

We are looking for a talented web designer to redevelop our sadly outdated website (www.brightlingua.net) to bring a fresh look with vastly increased functionality and web traffic.

Target Market(s)

-20s and 30s; mostly upper-middle class, educated
-from non-English speaking countries, but often have some English background
-looking to improve their English (mostly speaking) skills at our school like ours and experience living in a new country (like exchange students)

Industry/Entity Type

Education

Font styles to use
Sans Serif

Requirements
Must have
• - page listing our programs
- page with our fees and starting dates
- application form
- page showing why BRIGHT (us)?
- page with accommodation options
* responsive design
Nice to have
• examples of other websites in our industry I like:

http://www.halvorsenlang.com/
http://www.pqlearning.com/en
http://en.rtz.ca/
http://www.marstowe-academy.ac.uk/

```html
<!DOCTYPE html>
<html lang="en">
<head>
<meta charset="utf-8">
<title>Bright English – International Language School</title>
<link href="https://fonts.googleapis.com/css2?family=Roboto:wght@400;500;700&display=swap" rel="stylesheet">
<style>
:root{
  --ink:#222;
  --text:#666;
  --blue:#2f7ab3;
  --blue-mid:#3a88c2;
  --blue-link:#2a8ccc;
  --green-top:#9ad23a;
  --green-bot:#6fa81c;
  --dark:#1b1b1b;
  --nav-dark:#2a2a2a;
  --line:#dcdcdc;
  --white:#fff;
}
*{margin:0;padding:0;box-sizing:border-box}
html,body{width:1200px;height:2329px;overflow:hidden;background:var(--white)}
body{position:relative;font-family:"Roboto",Arial,sans-serif;color:var(--ink)}
.abs{position:absolute}

/* header */
.brand{left:88px;top:40px;display:flex;align-items:center;gap:10px}
.brand-dot{width:36px;height:36px;border-radius:50%;background:var(--blue-link)}
.brand-name{font-size:44px;font-weight:700;color:var(--ink);letter-spacing:-1px}
.lang{left:744px;top:42px;font-size:14px;color:#333;display:flex;align-items:center;gap:6px}
.flags{display:flex;gap:5px;margin-left:6px}
.flag{width:22px;height:14px;border:1px solid #ccc;display:flex}
.flag span{flex:1}
.phone{left:748px;top:90px;font-size:16px;color:#333;display:flex;align-items:center;gap:8px}
.search{left:915px;top:81px;width:196px;height:39px;border:1px solid #ccc;display:flex}
.search span{flex:1;font-size:11px;color:#333;padding:13px 12px}
.search b{width:30px;background:#1f5f99;display:flex;align-items:center;justify-content:center}

/* nav */
.nav{left:89px;top:163px;width:1022px;height:65px;background:linear-gradient(var(--green-top),var(--green-bot));display:flex}
.nav a{color:var(--white);text-decoration:none;font-size:14px;line-height:65px;padding:0 34px;text-transform:uppercase;white-space:nowrap}
.nav a.active{background:var(--nav-dark);padding:0 28px}

/* hero */
.hero-band{left:0;top:228px;width:1200px;height:573px;background:var(--dark)}
.slide{left:89px;top:250px;width:1022px;height:521px;border:3px solid var(--white);background:linear-gradient(100deg,#3b4a3a 0%,#7a6b5c 35%,#6c7f3a 65%,#1e2a1a 100%)}
.slide-caption{left:714px;top:552px;color:var(--white);font-family:"Roboto",Arial,sans-serif;font-weight:500;text-shadow:0 1px 3px rgba(0,0,0,.4)}
.slide-caption .s{font-size:25px;line-height:30px}
.slide-caption .l{font-size:33px;line-height:38px;margin-top:8px}
.slide-arrow{top:713px;width:32px;height:32px;border:2px solid var(--white);border-radius:50%}

/* features */
.features{left:89px;top:818px;width:1022px;height:169px;display:flex;box-shadow:0 14px 16px -10px rgba(0,0,0,.35)}
.feature{flex:1;background:var(--blue);display:flex;align-items:center;padding-left:30px;gap:18px}
.feature.mid{background:var(--blue-mid)}
.feature-icon{width:76px;height:76px;border-radius:50%;background:var(--white);flex:none;display:flex;align-items:center;justify-content:center}
.feature h3{color:var(--white);font-size:17px;font-weight:500;line-height:21px;text-transform:uppercase}
.feature p{color:#e6f0f8;font-size:12px;line-height:20px;margin-top:3px}
.btn-light{display:inline-block;margin-top:10px;background:linear-gradient(#fff,#d8d8d8);color:#333;font-size:10px;padding:6px 12px;border-radius:2px}

/* welcome */
.welcome{left:93px;top:1016px;width:540px}
.welcome h2{font-size:28px;font-weight:400}
.welcome h2 span{color:var(--blue-link)}
.welcome p{margin-top:14px;font-size:13px;line-height:24.5px;color:var(--text);text-align:justify}
.btn-dark{display:inline-block;margin-top:18px;background:var(--nav-dark);color:var(--white);font-size:16px;padding:11px 21px;border-radius:5px}
.video{left:681px;top:1010px;width:427px;height:260px;border:1px solid var(--line);padding:9px;box-shadow:0 1px 4px rgba(0,0,0,.15);background:var(--white)}
.video-screen{position:relative;width:100%;height:100%;background:linear-gradient(135deg,#3d4a33,#8a7a6a,#2c2c2c)}
.video-bar{position:absolute;left:0;right:0;bottom:0;height:34px;background:rgba(0,0,0,.8)}
.play{position:absolute;left:189px;top:77px;width:40px;height:40px;border-radius:50%;background:rgba(0,0,0,.5);border:2px solid rgba(255,255,255,.7)}

/* programs */
.programs{left:89px;top:1298px;width:1025px;height:360px;border:1px solid var(--line);background:#fafafa;box-shadow:0 10px 14px -8px rgba(0,0,0,.25)}
.programs h2{position:absolute;left:29px;top:18px;font-size:21px;font-weight:400}
.programs h2 span{color:var(--blue-link)}
.view-more{position:absolute;right:35px;top:24px;font-size:12px;color:var(--blue-link);text-decoration:underline}
.program{position:absolute;top:60px;width:313px}
.program-photo{height:177px;border:4px solid var(--white);box-shadow:0 0 3px rgba(0,0,0,.4)}
.program h3{margin-top:16px;font-size:17px;font-weight:400;color:var(--blue-link)}
.program p{margin-top:8px;width:300px;font-size:12px;line-height:22px;color:var(--text);text-align:justify}

/* students corner */
.corner{left:0;top:1687px;width:1200px;height:340px;background:linear-gradient(120deg,#5aaee0,#3d8fc9 50%,#5cb0e2)}
.corner h2{position:absolute;width:100%;top:31px;text-align:center;font-size:20px;font-weight:400;color:var(--ink)}
.circle-item{position:absolute;top:80px;width:170px;text-align:center}
.circle-photo{width:163px;height:163px;margin:0 auto;border-radius:50%;border:4px solid var(--white)}
.circle-item span{display:block;margin-top:22px;font-size:19px;color:var(--white)}

/* footer */
.footer-col{top:2063px}
.footer-col h4{font-size:13px;font-weight:400;color:var(--blue-link);text-transform:uppercase;margin-bottom:20px}
.footer-col p{font-size:11.5px;line-height:19.5px;color:#333}
.badges{display:grid;grid-template-columns:110px 60px;gap:14px 12px}
.badge{height:38px;background:#2d5fa8;border-radius:4px}
.badge.round{border-radius:50%;width:38px}
.links li{list-style:none;font-size:11.5px;color:#555;line-height:23px;padding-left:16px;position:relative}
.links li:before{content:"";position:absolute;left:2px;top:8px;border-left:6px solid #2a6aa0;border-top:4px solid transparent;border-bottom:4px solid transparent}
.social li{list-style:none;display:flex;align-items:center;gap:10px;font-size:11.5px;color:#555;margin-bottom:11px}
.social i{width:24px;height:24px;border-radius:50%;display:block}
.news-input{width:196px;height:38px;border:1px solid #bbb;font-size:11.5px;font-style:italic;color:#666;padding:11px 10px}
.btn-sub{display:inline-block;margin-top:16px;background:linear-gradient(#3f86c2,#225e95);color:var(--white);font-size:11.5px;padding:10px 20px;border-radius:3px}
.bottom-bar{left:0;top:2235px;width:1200px;height:94px;background:var(--dark);color:#eee;font-size:14px;text-align:center;line-height:94px}
</style>
</head>
<body>

<header>
  <div class="abs brand"><span class="brand-dot"></span><span class="brand-name">bright</span></div>
  <div class="abs lang">Access in your language :
    <span class="flags">
      <span class="flag"><span style="background:#1a9a3a"></span><span style="background:#fff"></span><span style="background:#ce2b37"></span></span>
      <span class="flag"><span style="background:#1d3f9a"></span><span style="background:#fff"></span><span style="background:#e0282e"></span></span>
      <span class="flag" style="flex-direction:column"><span style="background:#111"></span><span style="background:#d00"></span><span style="background:#fc0"></span></span>
      <span class="flag" style="background:#fff;align-items:center;justify-content:center"><i style="width:7px;height:7px;border-radius:50%;background:#c00;display:block"></i></span>
      <span class="flag"><span style="background:#0a6a3a"></span><span style="background:#fff"></span><span style="background:#c8102e"></span></span>
      <span class="flag" style="background:#139a43;align-items:center;justify-content:center"><i style="width:9px;height:9px;border-radius:50%;background:#fedf00;display:block"></i></span>
      <span class="flag" style="background:#fff;align-items:center;justify-content:center"><i style="width:7px;height:7px;border-radius:50%;background:linear-gradient(#c60c30 50%,#003478 50%);display:block"></i></span>
    </span>
  </div>
  <div class="abs phone">
    <svg width="22" height="22" viewBox="0 0 22 22"><circle cx="11" cy="11" r="10" fill="none" stroke="#2f7ab3" stroke-width="1.5"/><path d="M7 6c1-1 2 0 2.5 1.5l-1 1.2c.6 1.6 1.8 2.8 3.4 3.4l1.2-1c1.5.5 2.5 1.5 1.5 2.5-1 1.3-3 1-5.2-.8S5.7 7.3 7 6z" fill="#2f7ab3"/></svg>
    +1-416-555-0182
  </div>
  <div class="abs search"><span>Search</span><b><svg width="14" height="14" viewBox="0 0 14 14"><circle cx="6" cy="6" r="4.2" fill="none" stroke="#fff" stroke-width="1.8"/><path d="M9 9l4 4" stroke="#fff" stroke-width="2"/></svg></b></div>
</header>

<nav class="abs nav">
  <a class="active">Home</a><a>Our School</a><a>Programs</a><a>Free &amp; Dates</a><a>Accommodation</a><a>After Class</a><a>Agents</a>
</nav>

<section>
  <div class="abs hero-band"></div>
  <div class="abs slide" role="img" aria-label="Photo of smiling international students talking together"></div>
  <div class="abs slide-caption"><div class="s">OUR STUDENTS COME FROM</div><div class="l">AROUND THE WORLD</div></div>
  <svg class="abs slide-arrow" style="left:1011px" viewBox="0 0 32 32"><path d="M18 10l-6 6 6 6" fill="none" stroke="#fff" stroke-width="2.5"/></svg>
  <svg class="abs slide-arrow" style="left:1052px" viewBox="0 0 32 32"><path d="M14 10l6 6-6 6" fill="none" stroke="#fff" stroke-width="2.5"/></svg>
</section>

<section class="abs features">
  <div class="feature">
    <div class="feature-icon"><svg width="34" height="34" viewBox="0 0 34 34"><path d="M6 8l14 2 8 18-14-2z" fill="#c9a25c" stroke="#7a5a2a"/></svg></div>
    <div><h3>Easy Steps to Apply</h3><p>Lorem Ipsum is simply dummy<br>text of the printing</p><span class="btn-light">LEARN MORE</span></div>
  </div>
  <div class="feature mid">
    <div class="feature-icon"><svg width="34" height="34" viewBox="0 0 34 34"><rect x="7" y="6" width="20" height="22" fill="#f4d34a" stroke="#a88a1a"/><text x="13" y="23" font-size="14" font-family="Roboto, sans-serif" fill="#c0392b">?</text></svg></div>
    <div><h3>Frequently Ask<br>Question</h3><span class="btn-light">LEARN MORE</span></div>
  </div>
  <div class="feature">
    <div class="feature-icon"><svg width="34" height="34" viewBox="0 0 34 34"><rect x="6" y="10" width="22" height="15" fill="#f2c14e" stroke="#a07a1a"/><path d="M6 10l11 9 11-9" fill="none" stroke="#a07a1a"/></svg></div>
    <div><h3>Got a Question<br>Contact Us Now</h3><span class="btn-light">LEARN MORE</span></div>
  </div>
</section>

<section>
  <div class="abs welcome">
    <h2>WELCOME TO <span>BRIGHT ENGLISH</span></h2>
    <p>Lorem Ipsum has been the industry's standard dummy text ever since the 1500s, when an unknown printer took a galley of type and scrambled it to make a type specimen book. It has survived not only five centuries, but also the leap into electronic typesetting, remaining essentially unchanged. It was popularised in the 1960s with the release of Letraset sheets containing Lorem Ipsum passages, and more recently with desktop publishing software like Aldus PageMaker including versions of Lorem Ipsum.</p>
    <span class="btn-dark">Read More</span>
  </div>
  <div class="abs video">
    <div class="video-screen" role="img" aria-label="Video still of a group of students at the school">
      <span class="play"></span>
      <div class="video-bar"></div>
    </div>
  </div>
</section>

<section class="abs programs">
  <h2>OUR <span>PROGRAMS</span></h2>
  <span class="view-more">View More</span>
  <div class="program" style="left:26px">
    <div class="program-photo" role="img" aria-label="Photo of students writing at a desk" style="background:linear-gradient(135deg,#8a6a4a,#c9a88a)"></div>
    <h3>Full-Time Programs Intensive Focus</h3>
    <p>Lorem Ipsum has been the industry's standard dummy text ever since the 1500s, when an unknown printer took</p>
  </div>
  <div class="program" style="left:356px">
    <div class="program-photo" role="img" aria-label="Photo of a host family with a student at home" style="background:linear-gradient(135deg,#d8d4cc,#5a6a8a)"></div>
    <h3>Junior Programs Parent &amp; Child</h3>
    <p>Lorem Ipsum has been the industry's standard dummy text ever since the 1500s, when an unknown printer took</p>
  </div>
  <div class="program" style="left:687px">
    <div class="program-photo" role="img" aria-label="Photo of a class studying around a table" style="background:linear-gradient(135deg,#b89a6a,#6a5a4a)"></div>
    <h3>Special Programs University Bridge</h3>
    <p>Lorem Ipsum has been the industry's standard dummy text ever since the 1500s, when an unknown printer took</p>
  </div>
</section>

<section class="abs corner">
  <h2>STUDENTS' CORNER</h2>
  <div class="circle-item" style="left:107px"><div class="circle-photo" role="img" aria-label="Photo of a group of students" style="background:#8a5a5a"></div><span>Meet Our Students</span></div>
  <div class="circle-item" style="left:384px"><div class="circle-photo" role="img" aria-label="Photo of students at an event" style="background:#6a6a70"></div><span>Photo gallery</span></div>
  <div class="circle-item" style="left:666px"><div class="circle-photo" role="img" aria-label="Photo of a student studying" style="background:#9a8a80"></div><span>Lessons</span></div>
  <div class="circle-item" style="left:927px"><div class="circle-photo" role="img" aria-label="Photo of students relaxing" style="background:#8a7a6a"></div><span>News</span></div>
</section>

<footer>
  <div class="abs footer-col" style="left:92px">
    <h4>Company</h4>
    <div class="badges"><span class="badge"></span><span class="badge round"></span><span class="badge"></span><span class="badge round"></span></div>
  </div>
  <div class="abs footer-col" style="left:348px">
    <h4>Contact Us</h4>
    <p>412 Harbour Lane, Suite 105,<br>Toronto, Ontario, M4Y 1A1 Canada<br>Phone number: +1-416-555-0182<br>Fax number: +1-416-555-0183<br>E-mail: info@brightlingua.net</p>
  </div>
  <div class="abs footer-col" style="left:584px">
    <h4>Links</h4>
    <ul class="links"><li>Home</li><li>Our Team</li><li>Listings</li><li>Services</li></ul>
  </div>
  <div class="abs footer-col" style="left:731px">
    <h4>Connect Us</h4>
    <ul class="social"><li><i style="background:#3b5a98"></i>Friendsnet</li><li><i style="background:#2ba9e1"></i>Chirper</li><li><i style="background:#d34836"></i>Circleplus</li></ul>
  </div>
  <div class="abs footer-col" style="left:913px">
    <h4>Newsletter</h4>
    <div class="news-input">Enter Your Mail Id</div>
    <span class="btn-sub">SUBSCRIBE</span>
  </div>
  <div class="abs bottom-bar">Copyright © 2015 &nbsp;All Rights Reserved</div>
</footer>

</body>
</html>
```